Exciting Poster Project: 4 posters for Employee Benefit Program

We are an entrepreneurial healthcare IT company that is creating an internal campaign to launch our 2017 Culture and Professional Development goals for our internal staff.

We need 4 posters utilizing the 4 campaign logos (attached) that are tied together visually into a cohesive campaign.

A PPT is included that shows the other wall art that currently exists on the walls. The new posters will share a space with these pieces.

The posters may be mounted side by side, or stand alone on a wall- so the design should work both ways. Each poster should include its own icon and the tag line provided along with topics provided that fall under this category. The posters size can be dictated by your design, but the text should be legible from a minimum of 8 feet away.

At the bottom of each poster should include all 4 icons in order to tie the entire campaign together (perhaps they can be arranged together like a diamond shape with the primary one as the biggest diamond)

Our company website for our external branding is: www.pelmaroq.com
We have included our branding guidelines for our external brand, and ppts and graphics for our internal brand.

1) Poster 1:
a. Header: Better Today Than Yesterday
b. Sub-title: Personal and Professional Growth
c. Description: We are committed to helping you build on your strengths and passions and support you your career advancement goals. We have a variety of training and development programs available to help you reach your top potential!
Leadership Development Programs
1. Supervisor Training
2. Women’s Leadership
3. Leadership Meet-Ups
4. MBA Program
Staff Development
1. Continuing Education Fund
2. Book Club
3. Pelmaroq University
4. Mentorship
5. Learning Libraries
6. Department Wide Training Events

2) Poster 2:
a. Header: Perform at Highest Capacity
b. Sub-title: Be Your Best Self
c. Description: We are committed to providing programs that bring focus to your health and overall personal wellness to encourage a well balanced life
i. Healthy Living
1. Health and wellness seminars
2. Nutrition: Fruit Delivery
ii. Fitness:
1. Step Challenge
2. Virtual 5k
3. Recess
4. Golf Lessons
5. Ping Pong Club
iii. Creativity:
1. Painting
2. Photography Club
3. Virtual Trivia
iv. Mental Health:
1. Massage Therapy
2. EAP Education
v. Financial
1. 401(k)
2. Retirement education/financial planning seminars
3. Global Insurance Program education

3) Poster 3:
a. Header: Passionate Urgent and Driven to Success
b. Sub-Header: Innovation and Strategy
c. Description: We are committed to helping you connect the dots both in the industry and with our internal goals , mission, and vision.
i. Quarterly All-Hands
ii. Lumiverse
1. Internally: Departmental and Product Updates
2. Externally: Industry Knowledge
3. Culturally: Peer to Peer Community

4) Poster 4:
a. Header: Succeed as a Team
b. Sub-Header: Cultivating Collaboration
c. Description: We are committed to creating a culture of appreciation, teamwork, and supporting an open communication. All feedback and ideas are welcome here!
i. Team Building Events
1. Employee Focused
a. Summer Picnic
b. Employee Appreciation
c. Diwali
d. Holiday Party
e. Department Appreciation
2. Family Friendly
a. Halloween
b. Bring your Kids to Work Day
3. Awards
a. Peer to Peer: QuickNod Awards
b. Leadership: Crest of Merit
4. Surveys
a. New Hire
b. Employee Engagement
Updates

Target Market(s)

Internal Employees

Industry/Entity Type

Healthcare

Font styles to use
Sans Serif

Requirements
Must have
• Job Type: Posters
• Task Outline: Create Vector Art for 4 icons and 4 posters
• Fonts and Styles to Use: SourceSansPro
Nice to have
• There is an attachment with suggested concepts and styles that we like.
Should not have
• The poster should not be very wordy or hard to read in passing.

```html
<!DOCTYPE html>
<html lang="en">
<head>
<meta charset="utf-8">
<title>Passionate Urgent and Driven to Success</title>
<link rel="stylesheet" href="https://fonts.googleapis.com/css2?family=Source+Sans+3:wght@400;600;700&display=swap">
<style>
  :root {
    --navy: #1b2b54;
    --orange: #f05a28;
    --blue: #1e88c9;
    --grey: #4a4a4a;
    --paper: #ffffff;
    --amber: #f4a23a;
    --teal: #3a8fa6;
  }
  * { box-sizing: border-box; margin: 0; padding: 0; }
  html, body { width: 859px; height: 1200px; overflow: hidden; background: var(--paper); }
  body { font-family: "Source Sans 3", "Source Sans Pro", sans-serif; }
  .poster { position: relative; width: 859px; height: 1200px; overflow: hidden; background: var(--paper); }

  .hero-band {
    position: absolute; left: 0; top: 0; width: 859px; height: 415px;
    background: var(--navy);
  }
  .hero-art {
    position: absolute; left: 140px; top: 38px; width: 568px; height: 334px;
    border-radius: 24px;
    background: linear-gradient(90deg, var(--orange) 0%, #8a4a48 50%, var(--blue) 100%);
    opacity: 0.9;
  }

  .headline {
    position: absolute; left: 16px; top: 450px; width: 843px;
    font-weight: 700; font-size: 103px; line-height: 97px;
    color: var(--navy); letter-spacing: 0.6px;
  }
  .subhead {
    position: absolute; left: 16px; top: 731px;
    font-weight: 700; font-size: 50px; line-height: 56px;
    color: var(--orange);
  }
  .description {
    position: absolute; left: 20px; top: 792px; width: 818px;
    font-weight: 400; font-size: 29px; line-height: 38px;
    color: var(--grey);
  }
  .description .line { display: block; white-space: nowrap; }
  .description .line-first { text-align: justify; text-align-last: justify; white-space: normal; }
  .topics { position: absolute; left: 22px; top: 877px; list-style: none; }
  .topics li { font-size: 20.5px; line-height: 24.5px; color: var(--grey); }
  .topics .program { color: var(--orange); font-weight: 700; }

  .campaign-set {
    position: absolute; left: 30px; top: 1040px; width: 166px; height: 152px;
    border-radius: 18px;
    background: linear-gradient(135deg, var(--amber) 0%, var(--teal) 100%);
    opacity: 0.85;
  }

  .brand {
    position: absolute; left: 748px; top: 1097px; width: 100px;
    display: flex; flex-direction: column; align-items: center; gap: 8px;
  }
  .brand-mark { width: 62px; height: 62px; background: var(--orange); border-radius: 8px; }
  .brand-name { font-weight: 700; font-size: 22px; line-height: 24px; color: var(--navy); }
</style>
</head>
<body>
<main class="poster">
  <section class="hero-band">
    <div class="hero-art" role="img" aria-label="Orange heart holding an alarm clock beside a blue light bulb with a target and arrow"></div>
  </section>

  <h1 class="headline">Passionate Urgent and Driven to Success</h1>
  <h2 class="subhead">Innovation and Strategy</h2>
  <p class="description">
    <span class="line line-first">We are committed to helping you connect the dots both in the</span>
    <span class="line">industry and with our internal goals , mission, and vision.</span>
  </p>

  <ul class="topics">
    <li class="program">i. Quarterly All-Hands</li>
    <li class="program">ii. Lumiverse</li>
    <li>1. Internally: Departmental and Product Updates</li>
    <li>2. Externally: Industry Knowledge</li>
    <li>3. Culturally: Peer to Peer Community</li>
  </ul>

  <div class="campaign-set" role="img" aria-label="Set of the four campaign icons"></div>

  <div class="brand">
    <div class="brand-mark"></div>
    <span class="brand-name">Pelmaroq</span>
  </div>
</main>
</body>
</html>
```